Webdesign für Rheinau Vita Forschungsbund e.V.
Zielgruppe
Vereinsmitglieder aus der Bio-Tech-Branche, Öffentlichkeit
Aufgabenstellung
Wir benötigen ein Webdesign für die Website des Rheinau Vita Forschungsbund e.V., zu liefern als PSD-Datei.

```html
<!DOCTYPE html>
<html lang="de">
<head>
<meta charset="utf-8">
<title>Rheinau Vita Forschungsbund e.V.</title>
<link rel="stylesheet" href="https://fonts.googleapis.com/css2?family=Fira+Sans+Condensed:ital,wght@0,400;0,500;0,600;1,400;1,500&family=Fira+Sans:wght@400;500&display=swap">
<style>
  :root {
    --teal: #22c3ad;
    --teal-dark: #1db29d;
    --page: #e6e6e6;
    --panel: #ffffff;
    --text: #2b2b2b;
    --muted: #9a9a9a;
    --grey-band: #a9a9a9;
    --search-bg: #ecebec;
  }
  * { box-sizing: border-box; margin: 0; padding: 0; }
  html, body { width: 1200px; height: 1068px; overflow: hidden; }
  body {
    position: relative;
    background: linear-gradient(180deg, #dcdcdc 250px, #ececec 700px, #f4f4f4 1068px);
    font-family: "Fira Sans Condensed", "Fira Sans", sans-serif;
    color: var(--text);
  }
  .hero-backdrop {
    position: absolute; left: 0; top: 0; width: 1200px; height: 250px;
    background: linear-gradient(90deg, #8a9a3a 0%, #c9d0a0 8%, #e8e3dc 14%, #d94a2a 28%, #b8321c 50%, #3a1a12 64%, #7a2a18 76%, #c2471f 88%, #7aa22e 100%);
    filter: saturate(.85);
  }
  .hero-backdrop::after {
    content: ""; position: absolute; inset: 0;
    background: linear-gradient(180deg, rgba(255,255,255,0) 60%, rgba(220,220,220,.25) 100%);
  }
  .service-links {
    position: absolute; right: 120px; top: 32px;
    font-family: "Fira Sans", sans-serif; font-size: 12.5px; color: #fff;
    display: flex; gap: 7px;
  }
  .service-links span.sep { opacity: .9; }
  .panel {
    position: absolute; background: var(--panel);
    box-shadow: 0 1px 4px rgba(0,0,0,.22);
  }
  .header-frame { left: 120px; top: 57px; width: 960px; height: 283px; }
  .header-photo {
    position: absolute; left: 8px; top: 8px; width: 946px; height: 269px;
    background: radial-gradient(ellipse at 40% 40%, #dfe2ef 0%, #c3c7da 55%, #a9aec6 100%);
  }
  .logo-card {
    position: absolute; left: 218px; top: 43px; width: 382px; height: 139px;
    background: #fff; box-shadow: 0 1px 4px rgba(0,0,0,.25);
    display: flex; align-items: flex-end; justify-content: center; padding-bottom: 16px;
  }
  .logo-card .brand-name {
    font-family: "Fira Sans Condensed", sans-serif; font-weight: 500;
    font-size: 19px; letter-spacing: 1.6px; color: #2d2d2d; text-transform: uppercase;
  }
  .logo-card .brand-dot {
    position: absolute; left: 168px; top: 30px; width: 46px; height: 46px;
    border-radius: 50%; background: #4aa8b8;
  }
  .search-box { left: 120px; top: 360px; width: 232px; height: 57px; display: flex; align-items: center; padding-left: 20px; }
  .search-box label { color: var(--teal); font-size: 17px; font-weight: 500; }
  .search-box .field {
    margin-left: 15px; width: 140px; height: 28px; background: var(--search-bg);
    font-size: 13px; color: #555; line-height: 28px; padding-left: 10px;
  }
  .nav-box { left: 120px; top: 431px; width: 232px; height: 531px; overflow: hidden; }
  .nav-box svg { position: absolute; left: 0; top: 0; }
  .main-nav { position: absolute; left: 38px; top: 26px; list-style: none; }
  .main-nav > li { color: var(--teal); font-size: 16px; font-weight: 600; height: 43px; }
  .main-nav > li.has-sub { height: 95px; }
  .sub-nav { list-style: none; margin: 6px 0 0 17px; }
  .sub-nav li { color: var(--muted); font-size: 13.5px; font-weight: 400; line-height: 20px; }
  .intro-box { left: 375px; top: 360px; width: 705px; height: 182px; padding: 19px 26px 0 24px; }
  .intro-box p { font-size: 12.6px; line-height: 30px; text-align: justify; }
  .intro-box .drop { color: var(--teal); font-size: 22px; font-weight: 400; }
  .intro-box strong { font-weight: 600; }
  .more-link { position: absolute; right: 26px; bottom: 16px; color: var(--teal); font-size: 12.5px; }
  .members-box { left: 375px; top: 556px; width: 705px; height: 182px; }
  .members-photo {
    position: absolute; left: 21px; top: 18px; width: 216px; height: 145px;
    border: 4px solid #cfcfcf;
    background: radial-gradient(circle at 50% 45%, #8fb2cc 0%, #4f7797 55%, #2e4f6b 100%);
  }
  .members-box p {
    position: absolute; left: 269px; top: 17px; width: 412px;
    font-style: italic; font-size: 12.4px; line-height: 26px; color: var(--teal); text-align: justify;
  }
  .events-box { left: 375px; top: 753px; width: 705px; height: 209px; }
  .events-band {
    position: absolute; left: 368px; top: 769px; width: 719px; height: 37px;
    background: var(--grey-band); color: #fff; text-align: center;
    font-size: 19px; font-weight: 500; letter-spacing: 1px; line-height: 37px;
    box-shadow: 0 1px 2px rgba(0,0,0,.2);
  }
  .band-fold { position: absolute; top: 806px; }
  .event-list { position: absolute; left: 375px; top: 806px; width: 705px; height: 156px; display: flex; padding: 0 45px; }
  .event {
    flex: 1; text-align: center; position: relative;
  }
  .event + .event { border-left: 1px solid #ececec; }
  .event .date { margin-top: 24px; font-size: 13.5px; color: #8a8a8a; }
  .event .title { margin-top: 18px; font-size: 14px; font-weight: 600; color: #888; line-height: 18px; }
  .event .read { margin-top: 21px; font-size: 12px; font-style: italic; font-weight: 500; color: var(--teal); text-decoration: underline; letter-spacing: .6px; }
  .arrow { position: absolute; top: 868px; }
  .site-footer {
    position: absolute; left: 120px; top: 979px; width: 960px; height: 41px;
    background: var(--teal); color: #fff; font-size: 12.8px; font-weight: 600;
    display: flex; justify-content: flex-end; align-items: center; gap: 9px; padding-right: 40px;
  }
  .site-footer em { font-weight: 500; }
  .site-footer u { text-underline-offset: 2px; }
</style>
</head>
<body>
  <div class="hero-backdrop" role="img" aria-label="Unscharfes Hintergrundfoto in Rot- und Grüntönen"></div>

  <nav class="service-links">
    <span>Home</span><span class="sep">|</span><span>Impressum</span><span class="sep">|</span><span>Sitemap</span><span class="sep">|</span><span>RSS</span><span class="sep">|</span><span>Newsletter</span>
  </nav>

  <header class="panel header-frame">
    <div class="header-photo" role="img" aria-label="Foto von Wassertropfen auf einer hellblauen Fläche"></div>
  </header>

  <div class="logo-card">
    <span class="brand-dot"></span>
    <span class="brand-name">Rheinau Vita Forschungsbund</span>
  </div>

  <div class="panel search-box">
    <label>Suche</label>
    <div class="field">biotechnologie|</div>
  </div>

  <aside class="panel nav-box">
    <svg width="232" height="531" viewBox="0 0 232 531">
      <path d="M0 85 C 150 110, 210 260, 150 380 C 110 455, 50 490, 0 500" fill="none" stroke="#f1f1f1" stroke-width="34"/>
    </svg>
    <ul class="main-nav">
      <li>Startseite</li>
      <li class="has-sub">Über Uns
        <ul class="sub-nav"><li>Unterpunkt 1</li><li>Unterpunkt 2</li></ul>
      </li>
      <li>Mitglieder</li>
      <li>Region</li>
      <li>Service</li>
      <li>Kontakt</li>
      <li>Ansprechpartner</li>
    </ul>
  </aside>

  <section class="panel intro-box">
    <p><span class="drop">D</span>ie <strong>Rheinau Vita Forschungsbund</strong> versteht sich als Schrittmacher für die Biotechnologie-Region Rhein-Main. Wir sind qualifizierter Ansprechpartner für Unternehmen, Politik und Medien und Interessen-vertretung für alle, die in der Wertschöpfungskette von der Grundlagenforschung bis zum fertigen Produkt und seiner Vermarktung arbeiten. Hierfür bieten wir ein in der Region einzigartiges Netzwerk.</p>
    <span class="more-link">mehr lesen ...</span>
  </section>

  <section class="panel members-box">
    <div class="members-photo" role="img" aria-label="Foto von Luftblasen in blauem Wasser"></div>
    <p>In der Rheinau Vita Forschungsbund haben neben großen und mittelständischen Unternehmen auch eine große Zahl von Start-ups sowie Anwaltskanzleien, Patentanwälte, Venture-Capital- und Beratungsunternehmen zusammengefunden. Eine Übersicht über unsere Mitgliederstruktur gibt Ihnen unsere Datenbank. Sie können sie nach Kategorien oder nach Stichwörtern durchforsten.</p>
  </section>

  <section class="panel events-box"></section>
  <svg class="band-fold" style="left:368px" width="7" height="6"><polygon points="0,0 7,0 7,6" fill="#6f6f6f"/></svg>
  <svg class="band-fold" style="left:1080px" width="7" height="6"><polygon points="0,0 7,0 0,6" fill="#6f6f6f"/></svg>
  <h2 class="events-band">Veranstaltungen 2011</h2>
  <div class="event-list">
    <div class="event"><div class="date">17. Januar 2011</div><div class="title">Konferenz<br>Biotechnologie</div><div class="read">... weiterlesen</div></div>
    <div class="event"><div class="date">25. März 2011</div><div class="title">Weiterbildung<br>Netzwerk</div><div class="read">... weiterlesen</div></div>
    <div class="event"><div class="date">3. Mai 2011</div><div class="title">Meeting<br>Management</div><div class="read">... weiterlesen</div></div>
  </div>
  <svg class="arrow" style="left:388px" width="14" height="38"><polygon points="14,0 14,38 0,19" fill="#d6d6d6"/></svg>
  <svg class="arrow" style="left:1053px" width="14" height="38"><polygon points="0,0 0,38 14,19" fill="#d6d6d6"/></svg>

  <footer class="site-footer">
    <span>© Rheinau Vita Forschungsbund</span><span>|</span><em>Alle Rechte vorbehalten</em><span>|</span><u>Kontakt</u><span>|</span><u>Impressum</u>
  </footer>
</body>
</html>
```